Shine Bay Auto Care Business Card

2 side business card design for an auto detailing business

Target Market(s)

Auto detailing

Contact Information for Business Card

Things included

The business name “Shine Bay Auto Care”
Marc Tessier
(403)261-9047
Cedarvale, Sk

Services offered - complete interior& exterior detail
- paint correction & protection
- ceramic coating
- trim restore
- auto carpet & seat cleaning

Requirements
Must have
• Colours that are in my logo

Services offered

My name Marc Tessier
403-261-9047
Cedarvale, Sk

Not too sure in what order for these ?
Website. Shinebayautocare.com
Instagram Shinebayautocare
Email. Shinebayautoac@mailbox-example.com

```html
<!DOCTYPE html>
<html lang="en">
<head>
<meta charset="utf-8">
<title>Shine Bay Auto Care – Business Card</title>
<link rel="stylesheet" href="https://fonts.googleapis.com/css2?family=Open+Sans:ital,wght@0,400;0,600;0,700;0,800;1,400&display=swap">
<style>
  :root {
    --stage: #262626;
    --card-white: #ffffff;
    --card-black: #161616;
    --brand-red: #9b1b1f;
    --ink: #1d1d1d;
    --ink-soft: #4a4a4a;
    --text-light: #e9e9e9;
    --watermark: #f1e4e2;
  }
  * { box-sizing: border-box; margin: 0; padding: 0; }
  html, body {
    width: 1200px; height: 900px; overflow: hidden;
    background: var(--stage);
    font-family: "Open Sans", Arial, sans-serif;
  }
  .sheet {
    width: 1200px; height: 900px;
    display: flex; flex-direction: column; align-items: center; justify-content: center;
    gap: 48px;
  }
  .card {
    position: relative;
    width: 630px; height: 360px;
    overflow: hidden;
    box-shadow: 0 10px 30px rgba(0,0,0,.45);
  }

  /* Front */
  .card--front { background: var(--card-white); color: var(--ink); }
  .front-watermark {
    position: absolute; left: 330px; top: 215px;
    width: 320px; height: 320px; border-radius: 50%;
    border: 34px solid var(--watermark);
  }
  .brand {
    position: absolute; left: 48px; top: 40px;
    display: flex; align-items: center; gap: 14px;
  }
  .brand__dot {
    width: 46px; height: 46px; border-radius: 50%;
    background: var(--brand-red);
  }
  .brand__name {
    font-weight: 800; font-size: 27px; letter-spacing: .5px;
    color: var(--ink); line-height: 1.05; text-transform: uppercase;
  }
  .contact-list {
    position: absolute; left: 48px; top: 140px;
    list-style: none; font-size: 15px; line-height: 27px; color: var(--ink-soft);
  }
  .contact-list li { display: flex; align-items: center; gap: 10px; }
  .contact-list svg { width: 14px; height: 14px; flex: none; fill: var(--brand-red); }
  .holder {
    position: absolute; right: 48px; top: 140px; text-align: right;
  }
  .holder__name {
    font-weight: 800; font-size: 24px; line-height: 32px; color: var(--brand-red);
    text-transform: uppercase; letter-spacing: .5px;
  }
  .holder__role { font-size: 17px; line-height: 24px; color: var(--ink-soft); }

  /* Back */
  .card--back { background: var(--card-black); color: var(--text-light); }
  .back-brand {
    position: absolute; right: 56px; top: 48px;
    display: flex; align-items: center; gap: 12px;
  }
  .back-brand__dot { width: 34px; height: 34px; border-radius: 50%; background: var(--brand-red); }
  .back-brand__name {
    font-weight: 800; font-size: 20px; color: var(--brand-red); text-transform: uppercase;
  }
  .services {
    position: absolute; left: 48px; right: 40px; bottom: 56px;
    font-size: 17px; line-height: 28px; letter-spacing: .2px;
  }
  .services .sep { color: var(--brand-red); padding: 0 8px; font-weight: 700; }
</style>
</head>
<body>
<main class="sheet">

  <section class="card card--front" aria-label="Business card front">
    <div class="front-watermark" aria-hidden="true"></div>

    <div class="brand">
      <span class="brand__dot" aria-hidden="true"></span>
      <span class="brand__name">Shine Bay<br>Auto Care</span>
    </div>

    <ul class="contact-list">
      <li>
        <svg viewBox="0 0 24 24" aria-hidden="true"><path d="M6.6 10.8a15.1 15.1 0 0 0 6.6 6.6l2.2-2.2c.3-.3.7-.4 1-.2 1.1.4 2.3.6 3.6.6.6 0 1 .4 1 1V20c0 .6-.4 1-1 1A17 17 0 0 1 3 4c0-.6.4-1 1-1h3.5c.6 0 1 .4 1 1 0 1.3.2 2.5.6 3.6.1.3 0 .7-.2 1z"/></svg>
        403-261-9047
      </li>
      <li>
        <svg viewBox="0 0 24 24" aria-hidden="true"><path d="M2 5h20v14H2zm2 2v.4l8 5 8-5V7zm0 2.8V17h16V9.8l-8 5z"/></svg>
        Shinebayautoac@mailbox-example.com
      </li>
      <li>
        <svg viewBox="0 0 24 24" aria-hidden="true"><path d="M12 2a10 10 0 1 0 0 20 10 10 0 0 0 0-20zm0 2c.9 1.2 1.6 2.8 2 4.5h-4c.4-1.7 1.1-3.3 2-4.5zM4.3 14a8 8 0 0 1 0-4h3.5a16 16 0 0 0 0 4zm5.7 0a14 14 0 0 1 0-4h4a14 14 0 0 1 0 4zm6.2 0a16 16 0 0 0 0-4h3.5a8 8 0 0 1 0 4zM12 20c-.9-1.2-1.6-2.8-2-4.5h4c-.4 1.7-1.1 3.3-2 4.5z"/></svg>
        Shinebayautocare.com
      </li>
      <li>
        <svg viewBox="0 0 24 24" aria-hidden="true"><circle cx="12" cy="12" r="9"/></svg>
        Shinebayautocare
      </li>
      <li>
        <svg viewBox="0 0 24 24" aria-hidden="true"><path d="M12 2a7 7 0 0 0-7 7c0 5.3 7 13 7 13s7-7.7 7-13a7 7 0 0 0-7-7zm0 9.5A2.5 2.5 0 1 1 12 6.5a2.5 2.5 0 0 1 0 5z"/></svg>
        Cedarvale, Sk
      </li>
    </ul>

    <div class="holder">
      <p class="holder__name">Marc Tessier</p>
      <p class="holder__role">President</p>
    </div>
  </section>

  <section class="card card--back" aria-label="Business card back">
    <div class="back-brand">
      <span class="back-brand__dot" aria-hidden="true"></span>
      <span class="back-brand__name">Shine Bay Auto Care</span>
    </div>
    <div class="services">
      <p>complete interior&amp; exterior detail<span class="sep">•</span>paint correction &amp; protection</p>
      <p>ceramic coating<span class="sep">•</span>trim restore<span class="sep">•</span>auto carpet &amp; seat cleaning</p>
    </div>
  </section>

</main>
</body>
</html>
```